I need a Cool Physio Postcard / Flyer

HI!
We need a double sided, postcard sized, promotional card (not an actual postcard) to distribute to gyms and sporting clubs, promoting our physiotherapy clinic.
The main colours of our brand are navy blue & white (As seen in sample files).
I want it to be HORIZONTAL
On one side i'd like our logo / image.
The name - "Stride & Heel Recovery Collective" and the tagline - "“The nation's trusted lower-leg mending specialists.”
• Fast Rehab for lower limb injury and surgery
• Mobilisation of the foot and ankle
• Hands on therapy
• National sporting team expertise
• Podiatry (Toe-nail, skin, diabetic foot care, orthotics)
• Video pressure treadmill gait analysis and correction
• Running assessment
• Nordic walking training and sessions
Also our website: www.SHRC-example.com.au & a Facebook icon next to www.Facebook.com/SHRC
Also see the sample image of the runner and blue colouring. I would like this included somewhere on the postcard. I'd like to see some different design options implementing the image in different ways (front or back).
On the other side of the card I want the following text:
"SHRC is Victoria’s leading specialist provider of rehabilitation for Foot & Ankle injury and surgery.
We see our patients through their rehabilitation with an unmatched level of care and expertise.
Whether you’re an elite athlete, a weekend walker or strolling to the office, we provide the highest quality treatment and support to quickly get you back to your usual functional capacity, moving pain free with confidence.
Make an appointment at one of our FOUR Victorian locations today!”
Richmond
Brisk Motion Physio
Level 1, 417 Garnet St
Richmond 3121
1300 492 316 Frankston
Suite 6, 318 Wollaston Drive
Frankston 3199
9432 8155
Brighton
Suite 4, 187 Tern Street
Brighton 3186
9381 4027
Geelong
146 Pellham Terrace
Geelong 3220
5307 6491
Please display our four locations in a similar fashion to the white screenshot ive attached.
The images I included of my draft design are just to provide you an idea or some inspiration of what I’m after. Please feel free to use your creativity.. Good Luck!
Project Deadline Extended
Reason: I accidentally didn't put a design brief in for the first 6 days of the project. The designs only started arriving 4 days ago once I corrected this mistake.
I need more time to provide feedback & get exactly what I want.
Thanks in advance
Reid
Training

```html
<!DOCTYPE html>
<html lang="en">
<head>
<meta charset="utf-8">
<title>Stride &amp; Heel Recovery Collective – Promotional Card</title>
<link href="https://fonts.googleapis.com/css2?family=Lato:ital,wght@0,400;0,700;0,900;1,700;1,900&family=Crimson+Text:wght@400;700&display=swap" rel="stylesheet">
<style>
:root{
  --navy:#0d3a6b;
  --blue:#1a5a96;
  --blue-mid:#2a6fae;
  --blue-deep:#0a2f5a;
  --sky:#5aa0dc;
  --ink:#1c2a3a;
  --black:#111;
  --white:#fff;
  --paper:#f2f2f2;
  --stage:#e6e8eb;
}
*{box-sizing:border-box;margin:0;padding:0}
html,body{width:902px;height:1200px;overflow:hidden}
body{background:var(--stage);font-family:"Lato",sans-serif;position:relative}

.card{position:absolute;left:51px;width:800px;height:560px;background:var(--white);box-shadow:0 4px 14px rgba(0,0,0,.25);overflow:hidden}
.card--front{top:26px}
.card--back{top:614px}

/* front left */
.front-left{position:absolute;left:0;top:0;width:435px;height:560px}
.brand-header{height:96px;background:linear-gradient(90deg,var(--blue-deep),var(--blue-mid));color:var(--white);font-weight:700;font-size:27px;line-height:1.2;text-align:center;display:flex;align-items:center;justify-content:center;padding:0 20px;border-bottom:5px solid var(--white)}
.hero-photo{height:334px;background:linear-gradient(180deg,#5d7f9c 0%,#d9b59a 22%,#eaf3f8 45%,#7cc0e6 70%,#1f6fa8 100%)}
.tagline-band{height:76px;background:linear-gradient(90deg,var(--blue-deep),var(--blue-mid));color:var(--white);font-style:italic;font-weight:700;font-size:21px;line-height:1.3;text-align:center;display:flex;align-items:center;justify-content:center;padding:0 22px;border-top:4px solid var(--white)}
.web-strip{height:54px;display:flex;align-items:center;justify-content:center;color:var(--navy);font-weight:900;font-size:24px}

/* front right */
.front-right{position:absolute;left:435px;top:0;width:365px;height:560px}
.intro{height:96px;background:var(--white);font-family:"Crimson Text",serif;font-weight:700;font-size:17px;line-height:1.2;color:var(--black);text-align:center;display:flex;align-items:center;justify-content:center;padding:0 20px;border-bottom:3px solid var(--navy)}
.services{height:216px;background:linear-gradient(90deg,var(--blue-deep),var(--blue-mid));color:var(--white);font-size:13px;line-height:1.28;padding:8px 18px 0 28px;list-style:none}
.services li{position:relative;margin-bottom:6px}
.services li::before{content:"";position:absolute;left:-11px;top:6px;width:4px;height:4px;border-radius:50%;background:var(--white)}
.about{position:absolute;top:312px;left:0;right:0;bottom:0;background:linear-gradient(180deg,#fafafa,#e4e4e4);padding:10px 18px 0 26px}
.about-lead{color:var(--navy);font-size:18px;line-height:1.25;margin-bottom:10px}
.about-body{font-family:"Crimson Text",serif;font-size:13.5px;line-height:1.3;color:var(--ink);text-align:justify;margin-bottom:12px}
.about-cta{font-style:italic;font-weight:900;font-size:13px;line-height:1.35;color:var(--navy);text-transform:uppercase;width:200px}
.page-turn{position:absolute;right:0;bottom:0;width:100px;height:90px}
.page-turn-label{position:absolute;right:8px;bottom:10px;color:var(--white);font-weight:700;font-size:12px;text-align:right;line-height:1.3}

/* back */
.back-logo{position:absolute;top:20px;left:0;right:0;text-align:center;color:var(--blue);font-size:36px;font-weight:400}
.back-photo{position:absolute;top:84px;left:120px;right:120px;height:294px;background:radial-gradient(ellipse at center,#2e6f9e 0%,#5b8fb5 40%,#e9eef2 72%,#ffffff 100%)}
.locations{position:absolute;left:0;right:0;top:390px;bottom:0;display:grid;grid-template-columns:1fr 1fr;gap:0 2px;background:var(--white)}
.location{display:flex;flex-direction:column}
.location-name{height:28px;background:var(--black);color:var(--sky);font-family:"Crimson Text",serif;font-weight:700;font-size:19px;letter-spacing:.5px;text-transform:uppercase;text-align:center;line-height:28px;border-bottom:2px solid var(--white)}
.location-info{height:54px;background:linear-gradient(90deg,var(--blue-deep),var(--blue-mid),var(--blue-deep));color:var(--white);font-weight:700;font-size:12px;line-height:1.3;text-align:center;padding-top:5px;border-bottom:2px solid var(--white)}
.location-info svg{width:9px;height:9px;vertical-align:-1px;margin-right:4px;fill:var(--white)}
</style>
</head>
<body>

<section class="card card--front">
  <div class="front-left">
    <h1 class="brand-header">Stride &amp; Heel Recovery Collective</h1>
    <div class="hero-photo" role="img" aria-label="Silhouette of a woman running along a shoreline at sunrise, reflected in still blue water"></div>
    <p class="tagline-band">“The nation's trusted lower-leg mending specialists.”</p>
    <p class="web-strip">www.SHRC-example.com.au</p>
  </div>
  <div class="front-right">
    <h2 class="intro">SHRC is Victoria’s leading specialist provider of rehabilitation for Foot &amp; Ankle injury and surgery.</h2>
    <ul class="services">
      <li>Fast Rehab for lower limb injury and surgery</li>
      <li>Mobilisation of the foot and ankle</li>
      <li>Hands on therapy</li>
      <li>National sporting team expertise</li>
      <li>Podiatry (Toe-nail, skin and diabetic foot care, orthotics)</li>
      <li>Video pressure treadmill gait analysis and correction</li>
      <li>Running assessment</li>
      <li>Nordic walking training and sessions</li>
    </ul>
    <div class="about">
      <p class="about-lead">We see our patients through their rehabilitation with an unmatched level of care and expertise.</p>
      <p class="about-body">Whether you’re an elite athlete, a weekend walker or strolling to the office, we provide the highest quality treatment and support to quickly get you back to your usual functional capacity, moving pain free with confidence.</p>
      <p class="about-cta">Make an appointment at one of our four Victorian locations today!</p>
    </div>
    <svg class="page-turn" viewBox="0 0 100 90" aria-hidden="true">
      <polygon points="100,0 100,90 0,90" fill="#111"/>
      <path d="M100,0 C80,30 60,60 0,90 C30,70 20,40 30,20 C55,25 80,15 100,0Z" fill="#e9e9e9"/>
    </svg>
    <p class="page-turn-label">Turn to<br>Back page</p>
  </div>
</section>

<section class="card card--back">
  <h2 class="back-logo">Stride &amp; Heel Recovery Collective</h2>
  <div class="back-photo" role="img" aria-label="Pair of worn blue canvas high-top sneakers with black laces"></div>
  <div class="locations">
    <div class="location">
      <h3 class="location-name">Richmond</h3>
      <p class="location-info"><svg viewBox="0 0 10 10"><path d="M2 0l2 2-1 1.5c.8 1.5 2 2.7 3.5 3.5L8 6l2 2-1.5 2C4 9.5.5 6 0 1.5z"/></svg>1300 492 316<br><svg viewBox="0 0 10 10"><path d="M5 0l5 5H8.5v5h-2.5V7H4v3H1.5V5H0z"/></svg>Level 1, 417 Garnet St<br>Richmond 3121,</p>
    </div>
    <div class="location">
      <h3 class="location-name">Frankston</h3>
      <p class="location-info"><svg viewBox="0 0 10 10"><path d="M2 0l2 2-1 1.5c.8 1.5 2 2.7 3.5 3.5L8 6l2 2-1.5 2C4 9.5.5 6 0 1.5z"/></svg>9432 8155<br><svg viewBox="0 0 10 10"><path d="M5 0l5 5H8.5v5h-2.5V7H4v3H1.5V5H0z"/></svg>Suite 6, 318 Wollaston Drive<br>Frankston 3199</p>
    </div>
    <div class="location">
      <h3 class="location-name">Brighton</h3>
      <p class="location-info"><svg viewBox="0 0 10 10"><path d="M2 0l2 2-1 1.5c.8 1.5 2 2.7 3.5 3.5L8 6l2 2-1.5 2C4 9.5.5 6 0 1.5z"/></svg>9381 4027<br><svg viewBox="0 0 10 10"><path d="M5 0l5 5H8.5v5h-2.5V7H4v3H1.5V5H0z"/></svg>Suite 4, 187 Tern Street<br>Brighton 3186</p>
    </div>
    <div class="location">
      <h3 class="location-name">Geelong</h3>
      <p class="location-info"><svg viewBox="0 0 10 10"><path d="M2 0l2 2-1 1.5c.8 1.5 2 2.7 3.5 3.5L8 6l2 2-1.5 2C4 9.5.5 6 0 1.5z"/></svg>5307 6491<br><svg viewBox="0 0 10 10"><path d="M5 0l5 5H8.5v5h-2.5V7H4v3H1.5V5H0z"/></svg>146 Pellham Terrace<br>Geelong 3220</p>
    </div>
  </div>
</section>

</body>
</html>
```